International Health Supplement Company Needs Packaging and Label Redesign

Copper Lantern LLC requires a redesign for 1 internationally sold product and accompanying designs for 5 additional products. The additional products are currently sold locally and yet to be released internationally.

Our company is honest, premium, and passionate about supplements. We adopt a 'no BS' stance and as such source only the finest ingredients and deliver high-quality liquid health supplements to customers globally. We do not compromise on quality and do not apologise for price.

We want a clean, crisp design that conveys ‘premium, cutting-edge, boutique’ at a glance. We feel our current design appeals more to the 'chest beaters' rather than the 'chess players' that our research has indicated are our customers.

We have SIX PRODUCTS TOTAL in our range and feel individual color cues to distinguish the different products would greatly assist customer navigation i.e. Customers will identify ‘red’ means ‘product X’ without reading the label. (Examples attached and below we believe do this well).

Current 30ml bottle, cap, and dropper are in black and will remain so. Current label is black, however, we have a white label on our local product (example attached) and prefer the look of it.

Packaging is currently black and could remain so however most products that appeal to our target market are in white with color accents.

One consideration we have is that the product up until now has been selling exceptionally well so we need to retain some kind of familiarity with the existing branding. Perhaps that’s just the logo.

Logo can be revised i.e. add company name and/or company slogan.

Products are: (Function - Name)

Testosterone Support - Tongkat Ali (current)
Hormone Support - Jiaogulan
Energy Support - Ashwaghanda
Libido Support - Krachai Dam (for men)
Libido Support - Kacip Fatimah (for women)
Sleep Support - Wild Chamomile

Packaging: 4.6cm (L) x 8.0cm (W) x 11.2cm (H)
Label: 30 mL bottle

https://www.folioweb.example/gallery/TONIC-BOX-STUDY-2011/7402518
http://www.pelkastudio.example/projects/#/river-tea/
https://www.folioweb.example/gallery/31420786/Velmora-Skin
https://au.pinboardly.example/pin/592719083317915736/
https://au.pinboardly.example/pin/36916877689752218/
http://velto.example/en/portfolio/logo-redesign/

Target Market(s)

Generation X Men (and their partners), 36-55, upper middle class, who appreciate quality products.

Industry/Entity Type

Health Product

Font styles to use
Serif
Sans Serif

Requirements
Must have
• Packaging - Principal Display Panel (Front):
• 1. Function & Name of each product i.e 'Testosterone Support' & 'Tongkat Ali'
• 2. '30ml' AND '1 fl oz' (text size 1.8in / 3.2mm / 9 point min.)
• 3. 'Dietary Supplement'
• Packaging - Information Panel (Right):
• 1. Supplement Facts Panel (template accepted for drafts)
• 2. Directions: (lorum ipsum accepted for drafts)
• 3. Safety Warning: (lorum ipsum accepted for drafts)
• 4. 'Manufactured for: Copper Lantern LLC'
• 5. 'Sheridan, Wyoming'
• 6. '(414) 563 2180'
• 7. 'Product of Thailand'
• Bottle Label:
• 3. 'Dietary Supplement'
• 4. Supplement Facts Panel (template accepted for drafts)
• 5. Directions: (lorum ipsum accepted for drafts)
• 6. Safety Warning: (forum ipsum accepted for drafts)
• 7. 'Manufactured for: Copper Lantern LLC'
• 8. 'Sheridan, Wyoming'
• 9. '(414) 563 2180'
• 10. 'Product of Thailand'
Nice to have
• Updated logo with company name 'Copper Lantern' and/or company slogan 'Quality Without Compromise' added.
Should not have
• No photos or stock images.
• No elements of the current design (excluding logo) to remain i.e. 'Otter Finn', 'Testosterone Booster', 'Increase Lean Muscle', 'Stabilise Hormones', 'Boost Endurance', 'Improve Muscle Naturally', are all to be omitted.

```html
<!DOCTYPE html>
<html lang="en">
<head>
<meta charset="UTF-8">
<title>Tongkat Ali – Testosterone Support – Copper Lantern</title>
<link rel="stylesheet" href="https://fonts.googleapis.com/css2?family=Abril+Fatface&family=Saira+Extra+Condensed:wght@300;400&display=swap">
<style>
  :root {
    --red: #ee3f36;
    --ink: #3a3a3a;
    --ink-soft: #6a6a6a;
    --rule: #4a4a4a;
    --paper: #ffffff;
    --paper-shade: #eeeeee;
    --stage: #ffffff;
  }
  * { margin: 0; padding: 0; box-sizing: border-box; }
  html, body { width: 1200px; height: 1200px; overflow: hidden; background: var(--stage); }
  .canvas { position: relative; width: 1200px; height: 1200px; }

  .panel-text { position: absolute; inset: 0; width: 100%; height: 100%; overflow: visible; }
  .brand-dot { fill: var(--red); }
  .brand-name {
    font-family: "Saira Extra Condensed", "Arial Narrow", sans-serif; font-weight: 400;
    fill: var(--red); text-transform: uppercase; letter-spacing: 0.12em;
  }
  .product-name {
    font-family: "Abril Fatface", "Bodoni Moda", serif; fill: var(--red);
  }
  .function {
    font-family: "Saira Extra Condensed", "Arial Narrow", sans-serif; font-weight: 300;
    fill: var(--ink);
  }
  .meta {
    font-family: "Saira Extra Condensed", "Arial Narrow", sans-serif; font-weight: 300;
    fill: var(--ink-soft);
  }
  .rule { stroke: var(--rule); stroke-width: 2; }

  .label {
    position: absolute; left: 70px; top: 330px; width: 400px; height: 560px;
    background: linear-gradient(90deg, var(--paper) 60%, var(--paper-shade));
    display: flex;
  }
  .label__band { width: 42px; background: var(--red); flex: none; }
  .label__body { position: relative; flex: 1; }

  .carton {
    position: absolute; left: 520px; top: 160px; width: 620px; height: 880px;
    display: flex;
  }
  .carton__band { width: 190px; background: var(--red); flex: none; }
  .carton__face {
    position: relative; flex: 1;
    background: linear-gradient(90deg, var(--paper) 55%, var(--paper-shade));
  }
</style>
</head>
<body>
<main class="canvas">

  <section class="label" aria-label="Bottle label">
    <div class="label__band"></div>
    <div class="label__body">
      <svg class="panel-text" viewBox="0 0 358 560" xmlns="http://www.w3.org/2000/svg">
        <circle class="brand-dot" cx="38" cy="72" r="20"/>
        <text class="brand-name" x="68" y="80" font-size="24" textLength="190" lengthAdjust="spacingAndGlyphs">Copper Lantern</text>
        <text class="product-name" x="56" y="305" font-size="52" textLength="270" lengthAdjust="spacingAndGlyphs">TONGKAT</text>
        <text class="product-name" x="40" y="357" font-size="52" textLength="112" lengthAdjust="spacingAndGlyphs">ALI</text>
        <line class="rule" x1="70" y1="382" x2="340" y2="382"/>
        <text class="function" x="72" y="420" font-size="32" textLength="262" lengthAdjust="spacingAndGlyphs">TESTOSTERONE SUPPORT</text>
        <line class="rule" x1="70" y1="436" x2="340" y2="436"/>
        <text class="meta" x="72" y="478" font-size="22" textLength="168" lengthAdjust="spacingAndGlyphs">DIETARY SUPPLEMENT</text>
        <text class="meta" x="72" y="538" font-size="22" textLength="128" lengthAdjust="spacingAndGlyphs">1 FL OZ \ 30 ML</text>
      </svg>
    </div>
  </section>

  <section class="carton" aria-label="Carton front panel">
    <div class="carton__band" role="img" aria-label="Red side band with interlaced line pattern"></div>
    <div class="carton__face">
      <svg class="panel-text" viewBox="0 0 430 880" xmlns="http://www.w3.org/2000/svg">
        <circle class="brand-dot" cx="70" cy="112" r="28"/>
        <text class="brand-name" x="112" y="124" font-size="32" textLength="250" lengthAdjust="spacingAndGlyphs">Copper Lantern</text>
        <text class="product-name" x="60" y="560" font-size="66" textLength="330" lengthAdjust="spacingAndGlyphs">TONGKAT</text>
        <text class="product-name" x="36" y="626" font-size="66" textLength="140" lengthAdjust="spacingAndGlyphs">ALI</text>
        <line class="rule" x1="50" y1="660" x2="390" y2="660"/>
        <text class="function" x="50" y="706" font-size="40" textLength="336" lengthAdjust="spacingAndGlyphs">TESTOSTERONE SUPPORT</text>
        <line class="rule" x1="50" y1="724" x2="390" y2="724"/>
        <text class="meta" x="50" y="770" font-size="28" textLength="210" lengthAdjust="spacingAndGlyphs">DIETARY SUPPLEMENT</text>
        <text class="meta" x="50" y="836" font-size="28" textLength="160" lengthAdjust="spacingAndGlyphs">1 FL OZ \ 30 ML</text>
      </svg>
    </div>
  </section>

</main>
</body>
</html>
```